Automotive Accessories Business Card

Design a business template that match our new logo design and our industry.

https://www.kelvorauto.com/

Target Market(s)

Aftermarket auto parts and accessories

Industry/Entity Type

automotive

Contact Information for Business Card

company logo

Font styles to use
Serif
Sans Serif

Colors
EB3D1F
EC4F4E
F09395
F8D3D4
FCEDEE

```html
<!DOCTYPE html>
<html lang="en">
<head>
<meta charset="utf-8">
<title>Kelvor Auto Inc — Business Card</title>
<link href="https://fonts.googleapis.com/css2?family=Montserrat:wght@400;500;700;800&display=swap" rel="stylesheet">
<style>
  :root {
    --page: #ececec;
    --card: #3c3c3d;
    --card-deep: #333334;
    --red: #eb3d1f;
    --red-soft: #ec4f4e;
    --white: #ffffff;
    --text-light: #e9e9e9;
    --rule: #8a8a8a;
    --mark-grey: #8f8f90;
  }
  * { box-sizing: border-box; margin: 0; padding: 0; }
  html, body { width: 1200px; height: 802px; overflow: hidden; }
  body {
    background: var(--page);
    font-family: "Montserrat", sans-serif;
    position: relative;
  }
  .card {
    position: absolute;
    top: 252px;
    width: 520px;
    height: 298px;
    background: var(--card);
    border-bottom: 4px solid var(--red);
    border-right: 3px solid var(--red);
    box-shadow: 0 10px 24px rgba(0,0,0,0.18);
    overflow: hidden;
  }
  .card--front { left: 50px; }
  .card--back  { left: 630px; }

  /* Front */
  .brand {
    position: absolute;
    left: 34px;
    top: 120px;
    display: flex;
    align-items: center;
    gap: 9px;
    white-space: nowrap;
  }
  .brand__square { width: 14px; height: 14px; background: var(--red); flex: none; }
  .brand__name {
    color: var(--white);
    font-weight: 700;
    font-size: 16px;
    letter-spacing: 0.3px;
    text-transform: uppercase;
  }
  .divider {
    position: absolute;
    left: 272px;
    top: 70px;
    width: 1px;
    height: 158px;
    background: var(--rule);
  }
  .contact {
    position: absolute;
    left: 294px;
    top: 72px;
    color: var(--text-light);
    font-size: 12.5px;
    line-height: 1.35;
    white-space: nowrap;
  }
  .contact__name {
    color: var(--red);
    font-weight: 800;
    font-size: 16px;
    letter-spacing: 1.5px;
    text-transform: uppercase;
  }
  .contact__title { margin-bottom: 12px; }
  .contact__address { margin-bottom: 12px; }
  .contact__row { display: flex; align-items: center; gap: 8px; }
  .contact__row svg { width: 10px; height: 10px; fill: var(--red); flex: none; }

  /* Back */
  .mark {
    position: absolute;
    left: 34px;
    top: 48px;
    color: var(--mark-grey);
    font-weight: 800;
    font-size: 96px;
    line-height: 1;
    letter-spacing: -1px;
    opacity: 0.55;
    white-space: nowrap;
  }
  .back-brand {
    position: absolute;
    left: 40px;
    bottom: 52px;
    display: flex;
    align-items: center;
    gap: 12px;
  }
  .back-brand__square { width: 24px; height: 24px; background: var(--red); }
  .back-brand__name {
    background: var(--white);
    color: var(--card-deep);
    font-weight: 500;
    font-size: 26px;
    padding: 2px 12px;
    text-transform: uppercase;
    letter-spacing: 0.5px;
  }
</style>
</head>
<body>
  <section class="card card--front">
    <div class="brand">
      <span class="brand__square"></span>
      <span class="brand__name">Kelvor Auto Inc</span>
    </div>
    <div class="divider"></div>
    <div class="contact">
      <p class="contact__name">Daniel Reyes</p>
      <p class="contact__title">Manager</p>
      <p class="contact__address">240 W. Harbor Ave. Unit B<br>Riverton, CA 92210</p>
      <p class="contact__row">
        <svg viewBox="0 0 24 24" aria-hidden="true"><path d="M6.6 10.8a15 15 0 0 0 6.6 6.6l2.2-2.2a1 1 0 0 1 1-.25 11.4 11.4 0 0 0 3.6.57 1 1 0 0 1 1 1V20a1 1 0 0 1-1 1A17 17 0 0 1 3 4a1 1 0 0 1 1-1h3.5a1 1 0 0 1 1 1c0 1.25.2 2.45.57 3.57a1 1 0 0 1-.25 1z"/></svg>
        1-800-555-0142
      </p>
      <p class="contact__row">
        <svg viewBox="0 0 24 24" aria-hidden="true"><path d="M2 5h20v14H2zm2 2v.5l8 5 8-5V7l-8 5z"/></svg>
        sales@kelvorauto.com
      </p>
      <p class="contact__row">
        <svg viewBox="0 0 24 24" aria-hidden="true"><circle cx="12" cy="12" r="10"/></svg>
        www.kelvorauto.com
      </p>
    </div>
  </section>

  <section class="card card--back">
    <div class="mark">KELVOR</div>
    <div class="back-brand">
      <span class="back-brand__square"></span>
      <span class="back-brand__name">Kelvor Auto Inc</span>
    </div>
  </section>
</body>
</html>
```